Card design for home renovation company

We are a home renovation company looking for a card design with new logo. We look after every aspect of home renovation from design stage to completion.

Company name is, Brightwater Renovations

Target Market(s)

People wanting to have a home designed and built or renovated

Industry/Entity Type

Construction / Home Renovations

Contact Information for Business Card

Company name: Brightwater Renovations. Phone, email, website

Font styles to use
Serif
Sans Serif

Colors

Designer to choose only greyscale colors for use in the design.

Requirements
Must have
• Double sided card.
Nice to have
• A roofline logo integrated into the name

```html
<!DOCTYPE html>
<html lang="en">
<head>
<meta charset="utf-8">
<title>Brightwater Renovations – Business Card</title>
<link href="https://fonts.googleapis.com/css2?family=Poppins:wght@400;700&display=swap" rel="stylesheet">
<style>
  :root {
    --backdrop: #7a7a7a;
    --card-base: #262626;
    --accent-grey: #d4d4d4;
    --text-white: #ffffff;
  }
  * { box-sizing: border-box; margin: 0; padding: 0; }
  html, body {
    width: 1200px; height: 800px; overflow: hidden;
    background: var(--backdrop);
    font-family: "Poppins", sans-serif;
  }
  .canvas {
    position: relative; width: 1200px; height: 800px;
    display: flex; align-items: center; justify-content: center; gap: 40px;
  }
  .card {
    position: relative; width: 540px; height: 309px;
    background: var(--card-base); overflow: hidden;
  }

  /* Front side */
  .edge-tick { position: absolute; width: 5px; height: 14px; background: var(--accent-grey); }
  .edge-tick--left { left: 0; top: 220px; }
  .edge-tick--right { right: 0; top: 100px; }
  .front__name {
    position: absolute; left: 0; right: 0; top: 132px; text-align: center;
    color: var(--accent-grey); font-weight: 700; font-size: 22px; line-height: 1.2;
  }
  .front__web {
    position: absolute; left: 0; right: 0; bottom: 46px; text-align: center;
    color: var(--accent-grey); font-size: 10px;
  }

  /* Back side */
  .back__name {
    position: absolute; left: 36px; top: 154px;
    color: var(--accent-grey); font-weight: 700; font-size: 14.5px; line-height: 1.2;
    white-space: nowrap;
  }
  .back__divider {
    position: absolute; left: 276px; top: 18px; width: 2px; height: 240px;
    background: var(--text-white);
  }
  .person { position: absolute; left: 304px; top: 36px; }
  .person__name { color: var(--accent-grey); font-weight: 700; font-size: 16px; line-height: 1.25; }
  .person__title { color: var(--text-white); font-size: 10.5px; }
  .contacts { position: absolute; left: 308px; top: 116px; list-style: none; }
  .contacts__item {
    display: flex; align-items: center; gap: 10px; height: 38px;
    color: var(--text-white); font-size: 11px; white-space: nowrap;
  }
  .contacts__icon { width: 20px; height: 20px; flex: none; }
  .icon-ring { fill: none; stroke: var(--accent-grey); stroke-width: 1; }
  .icon-fill { fill: var(--text-white); }
  .icon-line { fill: none; stroke: var(--text-white); stroke-width: 0.8; }
  .icon-cut { fill: none; stroke: var(--card-base); stroke-width: 1; }
  .back__band {
    position: absolute; left: 0; right: 0; bottom: 0; height: 30px;
    background: var(--accent-grey);
  }
</style>
</head>
<body>
<main class="canvas">
  <section class="card card--front" aria-label="Card front">
    <span class="edge-tick edge-tick--left"></span>
    <span class="edge-tick edge-tick--right"></span>
    <h1 class="front__name">Brightwater Renovations</h1>
    <p class="front__web">www.brightwaterrenovations.com</p>
  </section>

  <section class="card card--back" aria-label="Card back">
    <p class="back__name">Brightwater Renovations</p>
    <span class="back__divider"></span>
    <div class="person">
      <p class="person__name">Sam Whitford</p>
      <p class="person__title">Marketing Coordinator</p>
    </div>
    <ul class="contacts">
      <li class="contacts__item">
        <svg class="contacts__icon" viewBox="0 0 20 20" aria-hidden="true">
          <circle class="icon-ring" cx="10" cy="10" r="9"/>
          <rect class="icon-fill" x="5.5" y="7" width="9" height="6.5"/>
          <path class="icon-cut" d="M5.5 7 L10 10.5 L14.5 7"/>
        </svg>
        sam.whitford@mail.com
      </li>
      <li class="contacts__item">
        <svg class="contacts__icon" viewBox="0 0 20 20" aria-hidden="true">
          <circle class="icon-ring" cx="10" cy="10" r="9"/>
          <path class="icon-fill" d="M7 5.5 L8.6 5.5 L9.3 7.8 L8.2 8.7 C8.8 10 9.9 11.1 11.2 11.7 L12.1 10.6 L14.4 11.3 L14.4 12.9 C14.4 13.5 13.9 14 13.3 14 C9.6 13.8 6.2 10.4 6 6.7 C6 6 6.5 5.5 7 5.5 Z"/>
        </svg>
        555 014 2290
      </li>
      <li class="contacts__item">
        <svg class="contacts__icon" viewBox="0 0 20 20" aria-hidden="true">
          <circle class="icon-ring" cx="10" cy="10" r="9"/>
          <circle class="icon-line" cx="10" cy="10" r="4.5"/>
          <ellipse class="icon-line" cx="10" cy="10" rx="2" ry="4.5"/>
          <path class="icon-line" d="M5.5 10 H14.5 M6.3 8 H13.7 M6.3 12 H13.7"/>
        </svg>
        www.brightwaterhomes.com
      </li>
    </ul>
    <span class="back__band"></span>
  </section>
</main>
</body>
</html>
```